buseisness card

design a card that similar to my web site
TRELLINGWORKSLLC .COM

Contact Information for Business Card

NAME PHONE # WEBSITE EMAIL AND DISCTIPTION OF WHAT WE DO

Colors
0054AA
0677BA
7BADD7
CADEEF
E8F1F8

Requirements
Must have
• lOGO AND DETAILS
Nice to have
• I LIKE THE WATER LIKE ON MY WEB SITE

```html
<!DOCTYPE html>
<html lang="en">
<head>
<meta charset="utf-8">
<title>Trelling Works — Business Card</title>
<link href="https://fonts.googleapis.com/css2?family=Montserrat:wght@400;500;600&display=swap" rel="stylesheet">
<style>
  :root {
    --backdrop: #d9dadc;
    --card-white: #f7f7f7;
    --brand-blue: #0a6fb0;
    --card-blue: #0b73ad;
    --ink-grey: #4a4d52;
    --rule-blue: #2a7fba;
    --white: #ffffff;
  }
  * { box-sizing: border-box; margin: 0; padding: 0; }
  html, body {
    width: 1200px; height: 800px; overflow: hidden;
    background: var(--backdrop);
    font-family: "Montserrat", sans-serif;
  }
  .sheet {
    width: 1200px; height: 800px;
    display: flex; flex-direction: column;
    align-items: center; justify-content: center; gap: 56px;
  }
  .card {
    width: 560px; height: 320px;
    border-radius: 22px;
    box-shadow: 0 6px 18px rgba(0,0,0,0.18);
    position: relative;
  }
  /* Front */
  .card-front { background: var(--card-white); display: flex; align-items: center; }
  .brand-block {
    width: 270px; display: flex; flex-direction: column; align-items: center; gap: 14px;
  }
  .brand-dot { width: 54px; height: 54px; border-radius: 50%; background: var(--brand-blue); }
  .brand-name {
    font-weight: 600; font-size: 24px; letter-spacing: 1px; color: var(--brand-blue);
  }
  .divider { width: 1px; height: 150px; background: var(--rule-blue); }
  .details { padding-left: 30px; color: var(--ink-grey); font-size: 12.5px; line-height: 1.45; }
  .person-name { font-weight: 600; font-size: 20px; color: var(--brand-blue); letter-spacing: 0.5px; line-height: 1.1; }
  .person-role { font-size: 12px; margin-bottom: 8px; }
  .address { margin-bottom: 8px; }
  .contact-line { display: flex; align-items: center; gap: 8px; }
  .contact-line svg { width: 12px; height: 12px; flex: none; }
  /* Back */
  .card-back {
    background: var(--card-blue);
    display: flex; flex-direction: column; align-items: center; justify-content: center; gap: 18px;
  }
  .card-back .brand-dot { width: 84px; height: 84px; background: var(--white); }
  .card-back .brand-name { color: var(--white); font-size: 36px; letter-spacing: 2px; }
</style>
</head>
<body>
<main class="sheet">
  <section class="card card-front">
    <div class="brand-block">
      <span class="brand-dot"></span>
      <span class="brand-name">TRELLING WORKS</span>
    </div>
    <div class="divider"></div>
    <div class="details">
      <p class="person-name">DANIEL MARSH</p>
      <p class="person-role">Founder &amp; CEO</p>
      <p class="address">4120 Cedar Hollow Road<br>Juneau, Alaska 99801</p>
      <p class="contact-line">
        <svg viewBox="0 0 24 24" aria-hidden="true"><path fill="#0a6fb0" d="M6.6 10.8a15 15 0 0 0 6.6 6.6l2.2-2.2a1 1 0 0 1 1-.25 11.4 11.4 0 0 0 3.6.57 1 1 0 0 1 1 1V20a1 1 0 0 1-1 1A17 17 0 0 1 3 4a1 1 0 0 1 1-1h3.5a1 1 0 0 1 1 1c0 1.25.2 2.45.57 3.57a1 1 0 0 1-.25 1z"/></svg>
        555-201-7789
      </p>
      <p class="contact-line">
        <svg viewBox="0 0 24 24" aria-hidden="true"><rect x="2" y="5" width="20" height="14" rx="2" fill="#0a6fb0"/><path d="M3 6l9 7 9-7" stroke="#fff" stroke-width="2" fill="none"/></svg>
        info@trellingworksllc.com
      </p>
      <p class="contact-line">
        <svg viewBox="0 0 24 24" aria-hidden="true"><circle cx="12" cy="12" r="10" fill="#0a6fb0"/><path d="M2 12h20M12 2c3 3 3 17 0 20M12 2c-3 3-3 17 0 20" stroke="#fff" stroke-width="1.5" fill="none"/></svg>
        trellingworksllc.com
      </p>
    </div>
  </section>

  <section class="card card-back">
    <span class="brand-dot"></span>
    <span class="brand-name">TRELLING WORKS</span>
  </section>
</main>
</body>
</html>
```